Website for Corvalind Capital, my new firm that raises money from investors to buy, build, own an...

Corvalind Capital needs a website! We are a new company with very experienced people, who invest in, own and build hotel properties, as well as apartments and other commercial real estate. We seek investors for our projects, and we provide safe, secure returns on their investment in our projects. Our new logo is designed to exhibit strength, class and security, and would like our website to continue on this theme. Our name, Corvalind, is a word-play on a Greek word “aristeia”, which means “excellence” and “a warriors finest moment of glory in war”. If you are in business, you realize that much of it is like war, with strategy and moves and opponents and competitors, and ever-changing economic conditions and threats that make business very much like war. We like to think that we are good at business (war), and so have named our company “Corvalind”, using the founders last name and the word “aristeia” combined. Another definition of "aristeia" is "performing at the peak of one's potential after a long struggle"...again, much like business in real life! The website design should exhibit financial security, smart moves, and positive growth towards a bright future.

Target Market(s)

The target market is smart and wealthy investors, with others such as brokers, cities and government agencies, lenders, sellers, partners, etc also looking at it.

Industry/Entity Type

Investment

Number of Pages Required

5+ page

Font styles to use
Sans Serif

Colors
fec214

Requirements
Must have
• Our website should have a landing page, a "about" or bio page, a projects page and a contact us page. Our new logo uses the colors black and gold, so this should be factored in to our site. The site should be simple, yet impactful and impressive. I have actually two logos, which can be mixed and interchanged in a complimentary way, each with their own unique look.
Nice to have
• I have uploaded a couple screenshots of a website i like, and the simplicity I mention.
Should not have
• The site should not be flashy or complicated or complex or "busy"

```html
<!DOCTYPE html>
<html lang="en">
<head>
<meta charset="utf-8">
<title>Corvalind Capital</title>
<link href="https://fonts.googleapis.com/css2?family=Lato:wght@400;700;900&display=swap" rel="stylesheet">
<style>
:root{
  --gold:#c59d45;
  --gold-soft:#b8974a;
  --ink:#1c1c1c;
  --white:#ffffff;
  --paper:#f7f5f1;
  --footer:#1b1b1b;
  --hero-dark:#2b2b2b;
}
*{margin:0;padding:0;box-sizing:border-box}
html,body{width:1200px;height:4833px;overflow:hidden}
body{font-family:"Lato",Arial,sans-serif;color:var(--ink);background:var(--white);position:relative}
.section{position:absolute;left:0;width:1200px;overflow:hidden}
.abs{position:absolute}
.center{left:0;width:1200px;text-align:center}
.photo{position:absolute;inset:0}
.eyebrow{font-weight:700;font-size:22px;letter-spacing:2px;text-transform:uppercase}
.rule{position:absolute;left:570px;width:60px;height:4px;background:var(--gold)}
.headline{font-weight:700;font-size:38px;line-height:49px}
.copy{font-weight:700;font-size:17px;line-height:22px}
.btn{position:absolute;height:44px;display:flex;align-items:center;justify-content:center;font-weight:700;font-size:20px;letter-spacing:2px;text-transform:uppercase}
.btn-dark{border:2px solid var(--ink);color:var(--ink);background:var(--white)}
.btn-light{border:2px solid var(--white);color:var(--white)}
.btn-gold-line{border:2px solid var(--gold);color:var(--gold)}
.btn-gold{background:var(--gold);color:var(--white)}

/* header */
.site-header{top:0;height:100px;background:var(--white)}
.brand{left:173px;top:34px;font-size:22px;letter-spacing:2px;font-weight:400;text-transform:uppercase;color:var(--ink)}
.brand span{border-left:2px solid var(--ink);padding-left:8px;margin-left:6px}
.nav{right:83px;top:38px;display:flex;gap:42px;font-weight:900;font-size:17px;letter-spacing:1px}

/* hero */
.hero{top:100px;height:690px;color:var(--white)}
.hero .photo{background:linear-gradient(180deg,#3a3a3a 0%,#5a5a5a 40%,#2a2a2a 100%)}
.hero .photo::after{content:"";position:absolute;inset:0;background:rgba(0,0,0,.35)}
.hero-title{font-size:46px;line-height:60px;font-weight:700;letter-spacing:1px}

/* projects */
.projects{top:790px;height:693px;background:var(--white)}
.section-title{font-weight:900;font-size:30px;letter-spacing:3px}
.service{position:absolute;top:205px;width:240px;text-align:center}
.service svg{display:block;margin:0 auto}
.service-label{margin-top:28px;font-weight:900;font-size:18px;text-transform:uppercase}

/* secure */
.secure{top:1483px;height:700px}
.secure .photo{height:660px;background:linear-gradient(120deg,#9a9a9a 0%,#6e6e6e 45%,#b0b0b0 100%)}
.secure-panel{left:173px;top:147px;width:854px;height:553px;background:rgba(45,45,45,.82);color:var(--white)}
.secure-panel .eyebrow,.secure-panel .headline{text-align:center;width:100%;position:absolute;left:0}

/* about */
.about{top:2143px;height:817px;background:var(--paper)}
.about .rule{background:var(--gold)}
.quote{font-weight:700;font-size:40px;line-height:54px}

/* strategy */
.strategy{top:2960px;height:817px;color:var(--white)}
.strategy .photo{background:linear-gradient(135deg,#444 0%,#2a2a2a 55%,#1b1b1b 100%)}
.strategy .rule{background:var(--gold)}

/* future */
.future{top:3777px;height:823px;color:var(--white)}
.future .photo{background:linear-gradient(180deg,#8d8250 0%,#7d6f3d 45%,#4f4224 80%,#3b3120 100%)}
.future .rule{background:var(--white)}

/* footer */
.site-footer{top:4600px;height:233px;background:var(--footer);color:var(--white)}
.address{left:190px;top:40px;font-weight:700;font-size:17px;line-height:22px}
.legal{left:190px;top:128px;font-weight:700;font-size:14px}
.partner-badge{left:633px;top:17px;width:94px;height:63px;background:var(--white)}
.social{left:633px;top:118px;display:flex;gap:26px}
.social span{width:30px;height:30px;border-radius:50%;background:var(--white);display:block}
</style>
</head>
<body>

<header class="section site-header">
  <div class="abs brand">Corvalind<span>Capital</span></div>
  <nav class="abs nav"><span>ABOUT US</span><span>PROJECT</span><span>FINANCE</span><span>CONTACT</span></nav>
</header>

<section class="section hero">
  <div class="photo" role="img" aria-label="Monochrome photo of a modern multi-storey hotel building under a cloudy sky"></div>
  <div class="abs center eyebrow" style="top:132px">The Gold of Management Capital</div>
  <div class="rule" style="top:167px;width:6px;left:597px;height:14px"></div>
  <h1 class="abs center hero-title" style="top:222px">Performing at the peak of one’s<br>potential after a long struggle</h1>
  <p class="abs center copy" style="top:373px;font-size:18px">Lorem ipsum dolor sit amet, consectetur adipiscing elit.<br>Donec pretium nisi malesuada porttitor iaculis. Suspendisse molestie nec sem<br>sed placerat. Nam massa tellus, blandit sed egestas cursus, lacinia id purus.<br>Donec pretium nisi malesuada porttitor iaculis.</p>
  <svg class="abs" style="left:555px;top:570px" width="90" height="30" viewBox="0 0 90 30"><polyline points="5,5 45,25 85,5" fill="none" stroke="var(--gold)" stroke-width="6"/></svg>
</section>

<section class="section projects">
  <h2 class="abs center section-title" style="top:74px">PROJECT WITH US</h2>
  <div class="rule" style="top:122px;width:110px;left:545px"></div>

  <div class="service" style="left:137px">
    <svg width="160" height="160" viewBox="0 0 160 160"><circle cx="80" cy="80" r="78" fill="var(--gold)"/><circle cx="80" cy="80" r="66" fill="none" stroke="#fff" stroke-width="3"/><circle cx="70" cy="58" r="14" fill="#fff"/><path d="M42 112c0-22 12-34 28-34s28 12 28 34z" fill="#fff"/><circle cx="102" cy="100" r="16" fill="var(--gold)" stroke="#fff" stroke-width="4"/><text x="102" y="108" font-family="Lato,sans-serif" font-weight="900" font-size="22" fill="#fff" text-anchor="middle">$</text></svg>
    <div class="service-label">Invesment</div>
  </div>
  <div class="service" style="left:373px">
    <svg width="160" height="160" viewBox="0 0 160 160"><circle cx="80" cy="80" r="78" fill="var(--gold)"/><circle cx="80" cy="80" r="66" fill="none" stroke="#fff" stroke-width="3"/><path d="M44 110h72M44 110V46" stroke="#fff" stroke-width="4" fill="none"/><rect x="54" y="88" width="10" height="20" fill="#fff"/><rect x="70" y="76" width="10" height="32" fill="#fff"/><rect x="86" y="66" width="10" height="42" fill="#fff"/><rect x="102" y="54" width="10" height="54" fill="#fff"/><polyline points="52,78 72,62 88,56 110,40" fill="none" stroke="#fff" stroke-width="3"/></svg>
    <div class="service-label">Finance</div>
  </div>
  <div class="service" style="left:600px">
    <svg width="160" height="160" viewBox="0 0 160 160"><circle cx="80" cy="80" r="78" fill="var(--gold)"/><circle cx="80" cy="80" r="66" fill="none" stroke="#fff" stroke-width="3"/><rect x="48" y="44" width="40" height="68" fill="#fff"/><g fill="var(--gold)"><rect x="54" y="52" width="8" height="8"/><rect x="74" y="52" width="8" height="8"/><rect x="54" y="68" width="8" height="8"/><rect x="74" y="68" width="8" height="8"/><rect x="54" y="84" width="8" height="8"/><rect x="74" y="84" width="8" height="8"/><rect x="63" y="98" width="10" height="14"/></g><circle cx="104" cy="96" r="16" fill="var(--gold)" stroke="#fff" stroke-width="4"/><text x="104" y="104" font-family="Lato,sans-serif" font-weight="900" font-size="22" fill="#fff" text-anchor="middle">$</text></svg>
    <div class="service-label">Property</div>
  </div>
  <div class="service" style="left:830px">
    <svg width="160" height="160" viewBox="0 0 160 160"><circle cx="80" cy="80" r="78" fill="var(--gold)"/><circle cx="80" cy="80" r="66" fill="none" stroke="#fff" stroke-width="3"/><polygon points="80,40 124,80 112,80 112,114 48,114 48,80 36,80" fill="#fff"/><rect x="72" y="90" width="16" height="24" fill="var(--gold)"/></svg>
    <div class="service-label">Real Estate</div>
  </div>

  <div class="btn btn-dark" style="left:440px;top:563px;width:320px">How to get started</div>
</section>

<section class="section secure">
  <div class="photo" role="img" aria-label="Black and white photo of a padlock resting beside rolled banknotes"></div>
  <div class="abs secure-panel">
    <div class="eyebrow" style="top:80px">Secure and Protection</div>
    <div class="rule" style="top:110px;left:397px;width:60px"></div>
    <h2 class="headline" style="top:143px">Reliable invesment protection<br>with accurate and always refined analysis<br>information technology</h2>
    <div class="btn btn-light" style="left:324px;top:363px;width:206px">Learn more</div>
    <svg class="abs" style="left:0;bottom:0" width="854" height="140" viewBox="0 0 854 140" preserveAspectRatio="none"><polygon points="0,90 854,0 854,140 0,140" fill="var(--gold)"/></svg>
  </div>
</section>

<section class="section about">
  <div class="abs center eyebrow" style="top:137px">About us</div>
  <div class="rule" style="top:173px"></div>
  <blockquote class="abs center quote" style="top:216px">“ Building commitment and communication<br>has a strong meaning in building<br>a sustainable business ”</blockquote>
  <p class="abs center copy" style="top:417px">Lorem ipsum dolor sit amet, consectetur adipiscing elit. Donec pretium nisi male-<br>suada porttitor iaculis. Suspendisse molestie nec sem sed placerat. Nam massa<br>tellus, blandit sed egestas cursus, lacinia id purus</p>
  <div class="abs center" style="top:517px;font-weight:900;font-size:20px;letter-spacing:1px">ELIAS MARROW</div>
  <div class="abs center" style="top:546px;font-weight:700;font-size:14px;color:var(--gold)">FOUNDER</div>
  <div class="btn btn-dark" style="left:507px;top:637px;width:190px">Our team</div>
</section>

<section class="section strategy">
  <div class="photo" role="img" aria-label="Dark photo of a hand moving a piece across a chessboard"></div>
  <div class="abs center eyebrow" style="top:137px">A Smart Move</div>
  <div class="rule" style="top:173px"></div>
  <h2 class="abs center headline" style="top:207px;font-size:40px;line-height:47px">Challenge after challenge in the era of<br>economic war made us strong in running<br>a business with vairous strategies<br>that worked appropriately</h2>
  <p class="abs center copy" style="top:437px">Lorem ipsum dolor sit amet, consectetur adipiscing elit. Donec pretium nisi male-<br>suada porttitor iaculis. Suspendisse molestie nec sem sed placerat. Nam massa<br>tellus, blandit sed egestas cursus, lacinia id purus</p>
  <div class="btn btn-gold-line" style="left:497px;top:640px;width:206px">Learn more</div>
</section>

<section class="section future">
  <div class="photo" role="img" aria-label="Warm golden photo of a group of people standing together in a field at sunset"></div>
  <div class="abs center eyebrow" style="top:120px">Invesment for the Future</div>
  <div class="rule" style="top:156px;width:70px;left:565px"></div>
  <h2 class="abs center headline" style="top:233px;font-size:40px;line-height:47px">We and you will always see a lot of<br>opportunities in every challenge by opening<br>the space to coma out staring ahead<br>that is more cheerful</h2>
  <p class="abs center copy" style="top:470px">Lorem ipsum dolor sit amet, consectetur adipiscing elit. Donec pretium nisi male-<br>suada porttitor iaculis. Suspendisse molestie nec sem sed placerat. Nam massa<br>tellus, blandit sed egestas cursus, lacinia id purus</p>
  <div class="btn btn-gold" style="left:333px;top:660px;width:207px;height:46px">Join us</div>
  <div class="btn btn-light" style="left:657px;top:660px;width:206px;height:46px">Contact us</div>
</section>

<footer class="section site-footer">
  <address class="abs address" style="font-style:normal">Brightmoor Lane 214<br>Harlow City, USA<br>T. +1 5550 184 327</address>
  <div class="abs legal">@2018 Corvalind All Right Reserved</div>
  <div class="abs partner-badge" role="img" aria-label="Partner badge"></div>
  <div class="abs social" aria-label="Social links"><span></span><span></span><span></span><span></span><span></span><span></span><span></span></div>
</footer>

</body>
</html>
```